(4) Bowling League Designs 1920x1080

Will be used on our website and in some digital signage.

We are starting (4) leagues this summer and need a basic graphic as an attention grab which will then lead the customer to full information / sign ups. The information I would need on each one is as follows:

1. Monday Night FREE ball league - Begins May 3rd

2. Tuesday Trios - KFDL Sanctioned - Begins May 11th
$9,000 prize fund

3. Wednesday Cosmic League - 9 pin no tap fun league - May 12th start

4. Thursday Night FREE ball league - Begins May 13th

I will attach some random examples of previous ones to give you an idea.

```html
<!DOCTYPE html>
<html lang="en">
<head>
<meta charset="utf-8">
<title>Summer Bowling Leagues</title>
<link rel="stylesheet" href="https://fonts.googleapis.com/css2?family=Roboto+Condensed:wght@400;700;800&family=Roboto:wght@400&display=swap">
<style>
  :root {
    --page-bg: #d9d9d9;
    --red-deep: #3d0204;
    --red-mid: #7e070b;
    --red-bright: #a80d12;
    --accent: #ee4550;
    --white: #ffffff;
    --date-box: rgba(10, 0, 0, 0.78);
    --row-band: rgba(30, 0, 0, 0.35);
  }
  * { margin: 0; padding: 0; box-sizing: border-box; }
  html, body { width: 1200px; height: 820px; overflow: hidden; background: var(--page-bg); }
  .league-board {
    position: absolute; left: 40px; top: 95px; width: 1120px; height: 630px;
    background:
      radial-gradient(ellipse at 85% 55%, var(--red-bright) 0%, transparent 60%),
      linear-gradient(100deg, var(--red-deep) 0%, var(--red-mid) 45%, var(--red-bright) 100%);
    overflow: hidden;
  }
  .league-row { position: absolute; left: 0; width: 780px; height: 118px; background: var(--row-band); }
  .start-date {
    position: absolute; left: 22px; top: 0; width: 170px; height: 118px;
    background: var(--date-box); padding: 14px 0 0 24px;
  }
  .start-date__label {
    display: block; font-family: "Roboto", sans-serif; font-weight: 400;
    font-size: 30px; letter-spacing: 3px; color: var(--accent); line-height: 1.1;
  }
  .start-date__day {
    display: block; font-family: "Roboto Condensed", sans-serif; font-weight: 800;
    font-size: 44px; color: var(--white); line-height: 1;
  }
  .league-title {
    position: absolute; left: 212px; top: 10px;
    font-family: "Roboto Condensed", sans-serif; font-weight: 800; text-transform: uppercase;
    color: var(--white); line-height: 1;
  }
  .league-title__main { display: block; font-size: 48px; }
  .league-title__sub { display: block; font-size: 40px; margin-top: 4px; }
  .league-title--small .league-title__main { font-size: 40px; margin-top: 8px; }
  .league-title--small .league-title__sub { font-size: 32px; margin-top: 6px; }
  .accent { color: var(--accent); }
  .prize-fund {
    position: absolute; left: 640px; top: 8px; width: 165px; height: 102px;
    background: var(--date-box); text-align: center; padding-top: 8px;
    font-family: "Roboto Condensed", sans-serif; font-weight: 700;
  }
  .prize-fund__amount { display: block; font-size: 50px; color: var(--white); line-height: 1; letter-spacing: -1px; }
  .prize-fund__label { display: block; font-size: 24px; color: var(--accent); margin-top: 6px; }
  .pin-art {
    position: absolute; right: 0; top: 40px; width: 330px; height: 560px;
    background: radial-gradient(ellipse at 50% 55%, #f4f0f0 0%, #d8cfcf 40%, rgba(168,13,18,0) 72%);
  }
</style>
</head>
<body>
  <main class="league-board">
    <section class="league-row" style="top:86px">
      <div class="start-date"><span class="start-date__label">BEGINS</span><span class="start-date__day">MAY 3</span></div>
      <h2 class="league-title"><span class="league-title__main">Monday <span class="accent">Night</span></span><span class="league-title__sub"><span class="accent">Free</span> Ball League</span></h2>
    </section>
    <section class="league-row" style="top:214px">
      <div class="start-date"><span class="start-date__label">BEGINS</span><span class="start-date__day">MAY 11</span></div>
      <h2 class="league-title"><span class="league-title__main">Tuesday <span class="accent">Trios</span></span><span class="league-title__sub"><span class="accent">KFDL</span> Sanctioned</span></h2>
      <div class="prize-fund"><span class="prize-fund__amount">$9,000</span><span class="prize-fund__label">PRIZE FUND</span></div>
    </section>
    <section class="league-row" style="top:342px">
      <div class="start-date"><span class="start-date__label">BEGINS</span><span class="start-date__day">MAY 12</span></div>
      <h2 class="league-title league-title--small"><span class="league-title__main">Wednesday <span class="accent">Cosmic League</span></span><span class="league-title__sub"><span class="accent">9 Pin</span> No Tap Fun League</span></h2>
    </section>
    <section class="league-row" style="top:470px">
      <div class="start-date"><span class="start-date__label">BEGINS</span><span class="start-date__day">MAY 13</span></div>
      <h2 class="league-title"><span class="league-title__main">Thursday <span class="accent">Night</span></span><span class="league-title__sub"><span class="accent">Free</span> Ball League</span></h2>
    </section>
    <div class="pin-art" role="img" aria-label="Bowling pins with red stripes and a red bowling ball"></div>
  </main>
</body>
</html>
```